Flyer-Design für Kaffeehaus
Zielgruppe
Wir sind ein Kaffeehaus und suchen ein super Design als Hintergrund für einen Jazz Brunch.
Zielgruppe Jung bis alt.
Aufgabenstellung
Schlicht, einfach, aber doch ausgefallen und modern.
Das Thema Jazz muss zwingend darin wiederSpiegeln und eventuell auch einen Hauch von Frühstück.
Jazz Bruch, live Jazz Musik mit Frühstück von 10-13 Uhr.
Ausgefallene aber leicht leserliche Schrift.
Benötigte Formate sind A6 A4 A3 und Titelbild und Profilbild Format für Facebook.

```html
<!DOCTYPE html>
<html lang="de">
<head>
<meta charset="utf-8">
<title>Jazz Brunch – Café Lindenhof Au</title>
<link href="https://fonts.googleapis.com/css2?family=Roboto+Slab:wght@700;800&family=Catamaran:wght@600;700&display=swap" rel="stylesheet">
<style>
  :root {
    --paper: #e7e3df;
    --orange: #e66a22;
    --brown: #663b16;
    --cream: #ece7e2;
  }
  html, body {
    margin: 0;
    padding: 0;
    width: 848px;
    height: 1200px;
    overflow: hidden;
    background: var(--paper);
  }
  .flyer {
    position: relative;
    width: 848px;
    height: 1200px;
    background: var(--paper);
    font-family: "Catamaran", "Helvetica Neue", Arial, sans-serif;
    color: var(--brown);
  }
  .sun {
    position: absolute;
    left: 127px;
    top: 102px;
    width: 554px;
    height: 554px;
    border-radius: 50%;
    background: var(--orange);
  }
  .art {
    position: absolute;
    border-radius: 30px;
    z-index: 1;
  }
  .art--saxophone {
    left: 50px; top: 72px; width: 160px; height: 306px;
    background: linear-gradient(160deg, #d9b79a, #b9825a);
    opacity: .85;
  }
  .art--tuba {
    left: 604px; top: 16px; width: 244px; height: 194px;
    background: linear-gradient(200deg, #dcc0a6, #b9825a);
    opacity: .85;
  }
  .art--notes {
    left: 500px; top: 80px; width: 116px; height: 160px;
    background: linear-gradient(180deg, #9b6a44, #663b16);
    opacity: .55;
  }
  .art--cup {
    left: 600px; top: 500px; width: 130px; height: 110px;
    background: linear-gradient(180deg, #efe6dc, #c9a584);
    border-radius: 18px 18px 44px 44px;
  }
  .title {
    position: absolute;
    left: 0;
    width: 808px;
    text-align: center;
    font-family: "Roboto Slab", Georgia, serif;
    font-weight: 800;
    color: var(--cream);
    margin: 0;
    line-height: 1;
    z-index: 2;
  }
  .title--jazz { top: 262px; font-size: 148px; letter-spacing: -2px; }
  .title--brunch { top: 412px; font-size: 80px; letter-spacing: 1px; }
  .tagline {
    position: absolute;
    top: 700px;
    left: 0;
    width: 848px;
    text-align: center;
    margin: 0;
    font-size: 38px;
    font-weight: 700;
    line-height: 1.2;
    letter-spacing: .5px;
  }
  .hours {
    position: absolute;
    top: 752px;
    left: 0;
    width: 814px;
    text-align: center;
    margin: 0;
    font-family: "Roboto Slab", Georgia, serif;
    font-weight: 700;
    font-size: 64px;
    line-height: 1.2;
    color: var(--orange);
  }
  .schedule {
    position: absolute;
    top: 864px;
    left: 0;
    width: 848px;
    height: 167px;
    background: var(--brown);
    display: grid;
    grid-template-columns: 289px 270px 289px;
    margin: 0;
    padding: 0;
    list-style: none;
  }
  .schedule__day {
    display: flex;
    flex-direction: column;
    align-items: center;
    justify-content: center;
    text-align: center;
    line-height: 1.05;
    margin: 32px 0;
  }
  .schedule__day + .schedule__day { border-left: 2px solid var(--cream); }
  .schedule__date { color: var(--orange); font-size: 30px; font-weight: 600; }
  .schedule__band { color: var(--cream); font-size: 31px; font-weight: 600; }
  .footer {
    position: absolute;
    top: 1112px;
    left: 0;
    width: 848px;
    height: 44px;
  }
  .footer__social {
    position: absolute;
    top: 12px;
    margin: 0;
    font-size: 15px;
    font-weight: 700;
    letter-spacing: .2px;
    white-space: nowrap;
  }
  .footer__social--instagram { left: 50px; }
  .footer__social--facebook { left: 560px; }
  .brand {
    position: absolute;
    left: 314px;
    top: 8px;
    width: 220px;
    display: flex;
    align-items: center;
    justify-content: center;
    gap: 8px;
    font-weight: 700;
    font-size: 20px;
    white-space: nowrap;
    color: var(--brown);
  }
  .brand__dot {
    width: 12px; height: 12px; border-radius: 50%;
    background: var(--brown);
    flex: none;
  }
</style>
</head>
<body>
  <main class="flyer">
    <div class="sun"></div>
    <div class="art art--saxophone" role="img" aria-label="Handgezeichnetes Saxophon"></div>
    <div class="art art--notes" role="img" aria-label="Gezeichnete Musiknoten"></div>
    <div class="art art--tuba" role="img" aria-label="Handgezeichnete Tuba"></div>

    <h1 class="title title--jazz">JAZZ</h1>
    <h2 class="title title--brunch">BRUNCH</h2>

    <div class="art art--cup" role="img" aria-label="Handgezeichnete Kaffeetasse"></div>

    <p class="tagline">LIVE JAZZ MUSIK MIT FRÜHSTÜCK</p>
    <p class="hours">10 – 13 Uhr</p>

    <ul class="schedule">
      <li class="schedule__day"><span class="schedule__date">27.06.20</span><span class="schedule__band">NAME BAND</span></li>
      <li class="schedule__day"><span class="schedule__date">28.06.20</span><span class="schedule__band">NAME BAND</span></li>
      <li class="schedule__day"><span class="schedule__date">29.06.20</span><span class="schedule__band">NAME BAND</span></li>
    </ul>

    <footer class="footer">
      <p class="footer__social footer__social--instagram">INSTAGRAM: CAFELINDENHOFAU</p>
      <div class="brand"><span class="brand__dot"></span>Café Lindenhof Au</div>
      <p class="footer__social footer__social--facebook">FACEBOOK: CAFÉ LINDENHOF AU</p>
    </footer>
  </main>
</body>
</html>
```